I need a shopify website for a beauty brand that i am starting. The name of the brand is called "Velna Beauty" i need the website to have a "Sleek Sexy And Mordern Design" preferable with a "Black Colour Scheme" i need the shopify store to be "Integrated With Instagram and Facebook" (@VelnaBeauty on Instagram and Velna Beauty On Facebook) ... I Also need to be able to "Easily to upload future products" (as ive only got three products at the moment) and i will also need to be "Able to capture emails to use for email marketing in the future as the brand grows "

```html
<!DOCTYPE html>
<html lang="en">
<head>
<meta charset="utf-8">
<title>Velna Beauty</title>
<link href="https://fonts.googleapis.com/css2?family=Playfair+Display:wght@400;700&family=Montserrat:wght@400;500;600;700&family=Great+Vibes&display=swap" rel="stylesheet">
<style>
:root{
  --black:#0b0b0b;
  --ink:#1a1a1a;
  --white:#ffffff;
  --grey:#8a8a8a;
  --light:#f2f2f2;
  --cyan:#19b5e6;
  --blue:#0b7fd6;
  --deep:#0a4fa8;
  --line:#2a2a2a;
}
*{margin:0;padding:0;box-sizing:border-box}
html,body{width:1200px;height:5172px;overflow:hidden}
body{position:relative;background:var(--white);font-family:"Montserrat",sans-serif;color:var(--ink)}
.abs{position:absolute}
.serif{font-family:"Playfair Display",serif}
.script{font-family:"Great Vibes",cursive}

/* top bar */
.topbar{left:0;top:0;width:1200px;height:32px;background:var(--black);border-bottom:1px solid var(--line);color:#bbb;font-size:11px}
.topbar .phone{left:100px;top:9px;display:flex;gap:8px;align-items:center}
.topbar .social{left:280px;top:9px;display:flex;gap:10px}
.topbar .social span{width:13px;height:13px;border-radius:50%;background:#777;display:block}
.topbar .account{right:100px;top:9px;display:flex;gap:0}
.topbar .account span{padding:0 14px;border-left:1px solid #333}

/* header */
.header{left:0;top:32px;width:1200px;height:136px;background:var(--black);color:var(--white)}
.brand{left:124px;top:42px;font-family:"Montserrat",sans-serif;font-weight:700;font-size:22px;letter-spacing:3px;text-transform:uppercase;color:var(--white)}
.nav{left:444px;top:58px;display:flex;gap:30px;font-size:12px;font-weight:600;letter-spacing:1px}
.header .icons{right:100px;top:52px;display:flex;gap:20px}

/* hero */
.hero{left:0;top:168px;width:1200px;height:592px;background:linear-gradient(100deg,#0c7dc9 0%,#22b8ec 45%,#5fcdf0 100%);overflow:hidden}
.hero .photo{right:0;top:0;width:640px;height:592px;background:radial-gradient(ellipse at 60% 55%,#e9c3b3 0%,#c99585 40%,#3d8fc5 75%,#1d86cc 100%)}
.hero .blob{left:90px;top:70px}
.hero .lashes{left:150px;top:150px;font-size:150px;color:var(--black);line-height:1}
.hero .beauty{left:150px;top:270px;font-size:110px;color:var(--white);letter-spacing:2px;line-height:1}
.hero .sub{left:120px;top:410px;width:330px;text-align:center;color:var(--white);font-size:14px;line-height:1.6}

/* section headings */
.heading{left:0;width:1200px;display:flex;justify-content:center;align-items:center;gap:22px;font-family:"Playfair Display",serif;font-size:42px;letter-spacing:1px}
.heading i{display:block;width:40px;height:2px;background:currentColor}
.subhead{left:0;width:1200px;text-align:center;font-size:13px;color:var(--grey)}

/* trend cards */
.trend{top:968px;width:248px;height:340px}
.trend .img{position:absolute;inset:0}
.trend .label{position:absolute;left:24px;right:24px;bottom:18px;height:64px;background:var(--white);text-align:center;padding-top:14px}
.trend .label b{display:block;font-size:15px;font-weight:600}
.trend .label small{font-size:10px;color:var(--grey)}

/* banner */
.banner{left:0;top:1472px;width:1200px;height:276px;background:var(--black)}
.banner .photo{left:100px;top:0;width:540px;height:276px;background:radial-gradient(ellipse at 35% 50%,#d8aa98 0%,#8a5c50 40%,#111 80%)}
.banner .frame{left:596px;top:24px;width:680px;height:220px;border:2px solid #cfcfcf}
.banner .title{left:660px;top:70px;width:560px;text-align:center;color:var(--white);font-size:54px}
.banner .text{left:760px;top:160px;width:360px;text-align:center;color:#ddd;font-size:14px;line-height:1.7}

/* products */
.product{width:248px;height:340px}
.product .img{position:absolute;left:0;top:0;width:248px;height:280px;background:var(--light)}
.product .lash{position:absolute;left:44px;top:100px;width:160px;height:60px;border-radius:50%;background:radial-gradient(ellipse,#3a3a3a 0%,#9a9a9a 55%,rgba(242,242,242,0) 75%)}
.product .label{position:absolute;left:20px;right:20px;top:258px;height:44px;background:var(--white)}
.product .name{position:absolute;left:0;width:248px;top:270px;text-align:center;font-size:15px;font-weight:600}
.product .price{position:absolute;left:0;width:248px;top:298px;text-align:center;font-size:11px;color:var(--grey);text-decoration:line-through}
.product .acts{position:absolute;left:0;width:248px;top:318px;display:flex;justify-content:center;gap:8px}
.badge{position:absolute;right:-14px;top:14px;width:54px;height:54px;border-radius:50%;color:var(--white);font-size:12px;font-weight:700;display:flex;align-items:center;justify-content:center}
.badge.new{background:var(--black)}
.badge.sale{background:var(--cyan)}

/* blog */
.blog{left:0;top:2920px;width:1200px;height:960px}
.blog .heading{color:var(--white);top:165px}
.post{top:3208px;width:408px;height:480px;background:var(--white)}
.post .img{position:absolute;left:0;top:0;width:408px;height:260px}
.post .meta{position:absolute;left:44px;top:296px;right:44px;display:flex;justify-content:space-between;font-size:11px;color:var(--grey)}
.post .meta .counts{display:flex;gap:14px}
.post h3{position:absolute;left:44px;top:330px;font-size:20px;font-weight:700}
.post p{position:absolute;left:44px;top:376px;width:310px;font-size:13px;color:#aaa;line-height:1.7}
.dots{left:572px;top:3752px;display:flex;gap:10px}

/* testimonials */
.testi-photo{left:0;top:3880px;width:640px;height:790px;background:radial-gradient(ellipse at 50% 45%,#e8c8b7 0%,#cfa08c 35%,#f6f6f6 72%)}
.reviews{left:740px;top:4030px;width:340px;text-align:center;font-size:64px;color:var(--ink)}
.testi-title{left:740px;top:4124px;width:340px;text-align:center;font-size:44px;letter-spacing:1px}
.avatar{left:868px;top:4196px;width:100px;height:100px;border-radius:50%;background:radial-gradient(circle,#e4bfae 0%,#b88776 60%,#8a5b4f 100%);border:4px solid #fff;box-shadow:0 0 0 1px #ddd}
.person{left:700px;top:4316px;width:440px;text-align:center;font-size:20px;font-weight:600}
.role{left:700px;top:4346px;width:440px;text-align:center;font-size:11px;color:var(--cyan)}
.quote{left:700px;top:4392px;width:440px;text-align:center;font-size:14px;color:var(--grey);line-height:1.7}
.qmark{left:895px;top:4450px}

/* footer */
.footer{left:0;top:4680px;width:1200px;height:492px;background:var(--black);color:#cfcfcf}
.footer .brand{top:70px;left:130px;font-size:22px}
.f-contact{left:130px;top:140px;font-size:12px;line-height:1.9;color:#bbb;width:260px}
.f-contact .row{display:flex;gap:10px;align-items:center}
.f-title{top:90px;font-size:22px;font-weight:700;color:var(--white)}
.f-links{left:500px;top:150px;width:200px;font-size:12px}
.f-links li{list-style:none;display:flex;gap:14px;align-items:center;height:44px;border-bottom:1px solid #2a2a2a}
.f-news{left:840px;top:150px;width:260px;font-size:12px;line-height:1.8;color:#bbb}
.f-input{left:840px;top:240px;width:220px;height:40px;border:1px solid #444;background:#111;color:#888;font-size:12px;padding:11px 14px}
.f-send{left:1060px;top:240px;width:44px;height:40px;background:var(--cyan);display:flex;align-items:center;justify-content:center}
.f-copy{left:840px;top:300px;font-size:11px;color:#999}
.f-copy b{color:var(--cyan);font-weight:500}
.f-social{left:840px;top:334px;display:flex;gap:12px}
.f-social span{width:16px;height:16px;border-radius:50%;background:#777;display:block}
</style>
</head>
<body>

<!-- top bar -->
<div class="abs topbar">
  <div class="abs phone">
    <svg width="11" height="11" viewBox="0 0 24 24" fill="#bbb"><path d="M6.6 10.8a15.1 15.1 0 006.6 6.6l2.2-2.2a1 1 0 011-.25 11.4 11.4 0 003.6.6 1 1 0 011 1V20a1 1 0 01-1 1A17 17 0 013 4a1 1 0 011-1h3.5a1 1 0 011 1 11.4 11.4 0 00.6 3.6 1 1 0 01-.25 1z"/></svg>
    +1 555 014 2290
  </div>
  <div class="abs social"><span></span><span></span></div>
  <div class="abs account"><span>My account</span><span>Help</span><span>Contact us</span><span>Delivery</span></div>
</div>

<!-- header -->
<header class="abs header">
  <div class="abs brand">Velna Beauty</div>
  <nav class="abs nav"><span>HOME</span><span>ABOUT</span><span>PRODUCTS</span><span>ACCESSORIES</span><span>SALE</span><span>CONTACT</span></nav>
  <div class="abs icons">
    <svg width="20" height="20" viewBox="0 0 24 24" fill="none" stroke="#fff" stroke-width="2"><circle cx="10" cy="10" r="7"/><path d="M15 15l6 6"/></svg>
    <svg width="20" height="20" viewBox="0 0 24 24" fill="none" stroke="#fff" stroke-width="2"><path d="M5 8h14l-1 13H6z"/><path d="M9 8a3 3 0 016 0"/></svg>
  </div>
</header>

<!-- hero -->
<section class="abs hero">
  <div class="abs photo" role="img" aria-label="Close-up of a model with long lashes and smoky eye makeup"></div>
  <svg class="abs blob" width="520" height="420" viewBox="0 0 520 420"><path d="M60 80 C140 0 360 10 440 70 C520 130 500 260 420 320 C340 390 170 420 90 350 C10 280 -10 150 60 80Z" fill="#4cd0f4" opacity=".55"/></svg>
  <div class="abs lashes script">Lashes</div>
  <div class="abs beauty serif">BEAUTY</div>
  <p class="abs sub">Duis sed odio sit amet nibh vulputate cursus a sit amet mauris morbi</p>
</section>

<!-- new design trends -->
<h2 class="abs heading" style="top:800px"><i></i>NEW DESIGN TRENDS<i></i></h2>
<p class="abs subhead" style="top:880px">Duis sed odio sit amet nibh vulputate cursus a sit amet mauris morbi</p>

<div class="abs trend" style="left:152px">
  <div class="img" role="img" aria-label="Model wearing deep shadow eye makeup" style="background:linear-gradient(160deg,#d9cfd1,#a48b86)"></div>
  <div class="label"><b>Deep Shadow</b><small>Shop Now</small></div>
</div>
<div class="abs trend" style="left:464px">
  <div class="img" role="img" aria-label="Model with curly hair showing eye lashes" style="background:linear-gradient(160deg,#c7ecf4,#8a5d48)"></div>
  <div class="label"><b>Eye Lashes</b><small>Shop Now</small></div>
</div>
<div class="abs trend" style="left:776px">
  <div class="img" role="img" aria-label="Blonde model with crystal clear look" style="background:linear-gradient(160deg,#f7c9d6,#e6b796)"></div>
  <div class="label"><b>Crystal Clear</b><small>Shop Now</small></div>
</div>

<!-- banner -->
<section class="abs banner">
  <div class="abs photo" role="img" aria-label="Model portrait with dramatic lashes"></div>
  <div class="abs frame"></div>
  <div class="abs title script">Lashes by Velna Beauty</div>
  <p class="abs text">Duis sed odio sit amet nibh vulputate cursus a sit amet mauris morbi</p>
</section>

<!-- products -->
<h2 class="abs heading" style="top:1916px"><i></i>OUR PRODUCTS<i></i></h2>

<div class="abs product" style="left:152px;top:2048px">
  <div class="img" role="img" aria-label="Pair of false eyelashes"><span class="lash"></span></div>
  <span class="badge new">NEW</span>
  <div class="label"></div><div class="name">Eye Lashes</div><div class="price">$39.00</div>
  <div class="acts"><svg width="12" height="12" viewBox="0 0 24 24" fill="none" stroke="#555" stroke-width="2"><path d="M7 10v11H3V10zM7 10l4-8a3 3 0 013 3v4h6l-2 12H7"/></svg><svg width="12" height="12" viewBox="0 0 24 24" fill="none" stroke="#555" stroke-width="2"><rect x="6" y="3" width="12" height="18"/><path d="M9 8h6"/></svg><svg width="12" height="12" viewBox="0 0 24 24" fill="none" stroke="#555" stroke-width="2"><path d="M5 8h14l-1 13H6z"/><path d="M9 8a3 3 0 016 0"/></svg></div>
</div>
<div class="abs product" style="left:464px;top:2048px">
  <div class="img" role="img" aria-label="Pair of false eyelashes"><span class="lash"></span></div>
  <div class="label"></div><div class="name">Eye Lashes</div><div class="price">$39.00</div>
  <div class="acts"><svg width="12" height="12" viewBox="0 0 24 24" fill="none" stroke="#555" stroke-width="2"><path d="M7 10v11H3V10zM7 10l4-8a3 3 0 013 3v4h6l-2 12H7"/></svg><svg width="12" height="12" viewBox="0 0 24 24" fill="none" stroke="#555" stroke-width="2"><rect x="6" y="3" width="12" height="18"/><path d="M9 8h6"/></svg><svg width="12" height="12" viewBox="0 0 24 24" fill="none" stroke="#555" stroke-width="2"><path d="M5 8h14l-1 13H6z"/><path d="M9 8a3 3 0 016 0"/></svg></div>
</div>
<div class="abs product" style="left:776px;top:2048px">
  <div class="img" role="img" aria-label="Pair of false eyelashes"><span class="lash"></span></div>
  <span class="badge sale">SALE</span>
  <div class="label"></div><div class="name">Eye Lashes</div><div class="price">$39.00</div>
  <div class="acts"><svg width="12" height="12" viewBox="0 0 24 24" fill="none" stroke="#555" stroke-width="2"><path d="M7 10v11H3V10zM7 10l4-8a3 3 0 013 3v4h6l-2 12H7"/></svg><svg width="12" height="12" viewBox="0 0 24 24" fill="none" stroke="#555" stroke-width="2"><rect x="6" y="3" width="12" height="18"/><path d="M9 8h6"/></svg><svg width="12" height="12" viewBox="0 0 24 24" fill="none" stroke="#555" stroke-width="2"><path d="M5 8h14l-1 13H6z"/><path d="M9 8a3 3 0 016 0"/></svg></div>
</div>
<div class="abs product" style="left:152px;top:2488px">
  <div class="img" role="img" aria-label="Pair of false eyelashes"><span class="lash"></span></div>
  <div class="label"></div><div class="name">Eye Lashes</div><div class="price">$39.00</div>
  <div class="acts"><svg width="12" height="12" viewBox="0 0 24 24" fill="none" stroke="#555" stroke-width="2"><path d="M7 10v11H3V10zM7 10l4-8a3 3 0 013 3v4h6l-2 12H7"/></svg><svg width="12" height="12" viewBox="0 0 24 24" fill="none" stroke="#555" stroke-width="2"><rect x="6" y="3" width="12" height="18"/><path d="M9 8h6"/></svg><svg width="12" height="12" viewBox="0 0 24 24" fill="none" stroke="#555" stroke-width="2"><path d="M5 8h14l-1 13H6z"/><path d="M9 8a3 3 0 016 0"/></svg></div>
</div>
<div class="abs product" style="left:464px;top:2488px">
  <div class="img" role="img" aria-label="Pair of false eyelashes"><span class="lash"></span></div>
  <span class="badge sale">SALE</span>
  <div class="label"></div><div class="name">Eye Lashes</div><div class="price">$39.00</div>
  <div class="acts"><svg width="12" height="12" viewBox="0 0 24 24" fill="none" stroke="#555" stroke-width="2"><path d="M7 10v11H3V10zM7 10l4-8a3 3 0 013 3v4h6l-2 12H7"/></svg><svg width="12" height="12" viewBox="0 0 24 24" fill="none" stroke="#555" stroke-width="2"><rect x="6" y="3" width="12" height="18"/><path d="M9 8h6"/></svg><svg width="12" height="12" viewBox="0 0 24 24" fill="none" stroke="#555" stroke-width="2"><path d="M5 8h14l-1 13H6z"/><path d="M9 8a3 3 0 016 0"/></svg></div>
</div>
<div class="abs product" style="left:776px;top:2488px">
  <div class="img" role="img" aria-label="Pair of false eyelashes"><span class="lash"></span></div>
  <div class="label"></div><div class="name">Eye Lashes</div><div class="price">$39.00</div>
  <div class="acts"><svg width="12" height="12" viewBox="0 0 24 24" fill="none" stroke="#555" stroke-width="2"><path d="M7 10v11H3V10zM7 10l4-8a3 3 0 013 3v4h6l-2 12H7"/></svg><svg width="12" height="12" viewBox="0 0 24 24" fill="none" stroke="#555" stroke-width="2"><rect x="6" y="3" width="12" height="18"/><path d="M9 8h6"/></svg><svg width="12" height="12" viewBox="0 0 24 24" fill="none" stroke="#555" stroke-width="2"><path d="M5 8h14l-1 13H6z"/><path d="M9 8a3 3 0 016 0"/></svg></div>
</div>

<!-- blog -->
<section class="abs blog">
  <svg class="abs" style="left:0;top:0" width="1200" height="960" viewBox="0 0 1200 960" role="img" aria-label="Blue toned close-up of a face behind the blog posts">
    <defs><linearGradient id="blogBlue" x1="0" y1="0" x2="0" y2="1"><stop offset="0" stop-color="#3aa6f2"/><stop offset=".5" stop-color="#0b7fe0"/><stop offset="1" stop-color="#0a5fc8"/></linearGradient></defs>
    <polygon points="0,60 600,8 1200,60 1200,900 600,952 0,900" fill="url(#blogBlue)"/>
    <polyline points="0,60 600,8 1200,60" fill="none" stroke="#0b0b0b" stroke-width="5"/>
    <polyline points="0,900 600,952 1200,900" fill="none" stroke="#0b0b0b" stroke-width="5"/>
  </svg>
  <h2 class="abs heading"><i></i>FROM THE BLOG<i></i></h2>
</section>

<article class="abs post" style="left:152px">
  <div class="img" role="img" aria-label="Model with dark hair for the new collection post" style="background:linear-gradient(135deg,#e9e9e9,#6d5a55 60%,#2a2222)"></div>
  <div class="meta"><span>21 Dec 2021</span><span class="counts"><span>♡ 5</span><span>◯ 3</span></span></div>
  <h3>New Collection</h3>
  <p>Sed sed odio sit amet nibh vulputate cursus a sit amet mauris morbi</p>
</article>
<article class="abs post" style="left:628px">
  <div class="img" role="img" aria-label="Model by a window for the latest products post" style="background:linear-gradient(135deg,#f2f2f2,#c9b2a6 55%,#4a3a34)"></div>
  <div class="meta"><span>21 Dec 2021</span><span class="counts"><span>♡ 5</span><span>◯ 3</span></span></div>
  <h3>Latest Products</h3>
  <p>Sed sed odio sit amet nibh vulputate cursus a sit amet mauris morbi</p>
</article>
<div class="abs dots">
  <svg width="12" height="10" viewBox="0 0 12 10"><path d="M8 1L3 5l5 4" fill="none" stroke="#fff" stroke-width="2"/></svg>
  <svg width="12" height="10" viewBox="0 0 12 10"><path d="M4 1l5 4-5 4" fill="none" stroke="#fff" stroke-width="2"/></svg>
</div>

<!-- testimonials -->
<div class="abs testi-photo" role="img" aria-label="Smiling model with hand near her face"></div>
<div class="abs reviews script">Reviews</div>
<h2 class="abs testi-title serif">TESTIMONIALS</h2>
<div class="abs avatar" role="img" aria-label="Customer portrait"></div>
<div class="abs person">Marla Quinn</div>
<div class="abs role">Customer</div>
<p class="abs quote">Duis sed odio sit amet nibh vulputate cursus a sit amet<br>mauris morbi Duis sed odio sit amet nibh vulputate<br>cursus a sit amet mauris morbi</p>
<svg class="abs qmark" width="50" height="40" viewBox="0 0 50 40"><path d="M4 38V22C4 10 10 4 20 2l2 5c-6 2-9 6-9 11h8v20zM28 38V22c0-12 6-18 16-20l2 5c-6 2-9 6-9 11h8v20z" fill="#19b5e6"/></svg>

<!-- footer -->
<footer class="abs footer">
  <div class="abs brand">Velna Beauty</div>
  <div class="abs f-contact">
    <div>412 Larkspur Lane, Fairmont,<br>OR 97120, United States</div>
    <div style="height:16px"></div>
    <div class="row"><span style="color:#19b5e6">✆</span>Phone: +1 555 014 2290</div>
    <div class="row"><span style="color:#19b5e6">✆</span>Fax: +1 555 014 2291</div>
    <div class="row"><span style="color:#19b5e6">✉</span>Email: hello@velnabeauty.shop</div>
  </div>

  <div class="abs f-title" style="left:500px">Useful Links</div>
  <ul class="abs f-links">
    <li><svg width="10" height="10" viewBox="0 0 10 10"><path d="M1 5l3 3 5-6" fill="none" stroke="#19b5e6" stroke-width="1.6"/></svg>Home</li>
    <li><svg width="10" height="10" viewBox="0 0 10 10"><path d="M1 5l3 3 5-6" fill="none" stroke="#19b5e6" stroke-width="1.6"/></svg>About</li>
    <li><svg width="10" height="10" viewBox="0 0 10 10"><path d="M1 5l3 3 5-6" fill="none" stroke="#19b5e6" stroke-width="1.6"/></svg>Products</li>
    <li><svg width="10" height="10" viewBox="0 0 10 10"><path d="M1 5l3 3 5-6" fill="none" stroke="#19b5e6" stroke-width="1.6"/></svg>Accessories</li>
    <li><svg width="10" height="10" viewBox="0 0 10 10"><path d="M1 5l3 3 5-6" fill="none" stroke="#19b5e6" stroke-width="1.6"/></svg>Sale</li>
    <li><svg width="10" height="10" viewBox="0 0 10 10"><path d="M1 5l3 3 5-6" fill="none" stroke="#19b5e6" stroke-width="1.6"/></svg>Contact</li>
  </ul>

  <div class="abs f-title" style="left:840px">Newsletter</div>
  <p class="abs f-news">Duis sed odio sit amet nibh vulputate<br>cursus a sit amet mauris morbi</p>
  <div class="abs f-input">Email address</div>
  <div class="abs f-send"><svg width="16" height="16" viewBox="0 0 24 24" fill="#fff"><path d="M2 21l21-9L2 3v7l15 2-15 2z"/></svg></div>
  <div class="abs f-copy">2021 © Copyrights <b>Velna Beauty</b></div>
  <div class="abs f-social"><span></span><span></span></div>
</footer>

</body>
</html>
```